New Zealand Marlborough Sauvignon Blanc wine packaging design

We need packaging design for our new wine brand, Dunmore Hale. The wine is a New Zealand Marlborough Sauvignon Blanc. We would like the packaging will portray elegance and style with an understated label. We are looking for a label that portrays the elegance of the French Riviera. The label should be round or pill shaped.
Updates

Industry/Entity Type

Wine

Font styles to use
Serif
Sans Serif

Requirements
Must have
• The words in order of importance: Dunmore Hale, Sauvignon Blanc, Marlborough, New Zealand. It should be fit to the bottle posted in the links
Nice to have
• a pill shape or circular shape
Should not have
• Illustrations of wine bottles, wine glasses, or grapes

```html
<!DOCTYPE html>
<html lang="en">
<head>
<meta charset="utf-8">
<title>Dunmore Hale — Sauvignon Blanc Label</title>
<link rel="stylesheet" href="https://fonts.googleapis.com/css2?family=DM+Serif+Text&family=Source+Serif+4:wght@600&display=swap">
<style>
  :root {
    --page-bg: #f3f3f1;
    --label-paper: #f2f0e3;
    --label-ink: #4b4a3d;
    --scene-light: #f4f2e6;
    --scene-shade: #e6e3d2;
  }
  html, body {
    margin: 0;
    padding: 0;
    width: 900px;
    height: 1200px;
    overflow: hidden;
    background: var(--page-bg);
  }
  .label {
    display: block;
    width: 900px;
    height: 1200px;
  }
  .label-paper { fill: var(--label-paper); }
  .label-rule { fill: none; stroke: var(--label-ink); stroke-width: 2.5; }
  .arc-text {
    font-family: "Source Serif 4", Georgia, serif;
    font-weight: 600;
    fill: var(--label-ink);
  }
  .varietal { font-size: 30px; letter-spacing: 1px; }
  .region { font-size: 30px; letter-spacing: 1px; }
  .side-band { font-size: 17px; }
  .brand-name {
    font-family: "DM Serif Text", Georgia, serif;
    font-size: 52px;
    fill: var(--label-ink);
  }
  .volume {
    font-family: "Source Serif 4", Georgia, serif;
    font-weight: 600;
    font-size: 12px;
    fill: var(--label-ink);
  }
</style>
</head>
<body>
<svg class="label" viewBox="0 0 900 1200" xmlns="http://www.w3.org/2000/svg" aria-label="Dunmore Hale Sauvignon Blanc label">
  <defs>
    <linearGradient id="scene-tone" x1="0" y1="0" x2="0" y2="1">
      <stop offset="0" stop-color="var(--scene-light)"/>
      <stop offset="1" stop-color="var(--scene-shade)"/>
    </linearGradient>
    <path id="top-arc" d="M 222 430 A 228 228 0 0 1 678 430"/>
    <path id="bottom-arc" d="M 212 770 A 238 238 0 0 0 688 770"/>
    <path id="left-band" d="M 240 860 L 240 340"/>
    <path id="right-band" d="M 672 340 L 672 860"/>
  </defs>

  <!-- pill label -->
  <rect class="label-paper" x="180" y="160" width="540" height="880" rx="270"/>
  <rect class="label-rule" x="192" y="172" width="516" height="856" rx="258"/>

  <!-- coastal scene window -->
  <rect x="282" y="283" width="336" height="660" rx="168" fill="url(#scene-tone)"
        role="img" aria-label="Line drawing of a coastal bay with rolling hills, sea and a beach parasol"/>
  <rect class="label-rule" x="282" y="283" width="336" height="660" rx="168"/>

  <!-- curved text -->
  <text class="arc-text varietal" text-anchor="middle">
    <textPath href="#top-arc" startOffset="50%">Sauvignon Blanc</textPath>
  </text>
  <text class="arc-text region" text-anchor="middle">
    <textPath href="#bottom-arc" startOffset="50%">Marlborough, New Zealand</textPath>
  </text>
  <text class="arc-text side-band">
    <textPath href="#left-band" textLength="500">Dunmore Hale Dunmore Hale Dunmore Hale</textPath>
  </text>
  <text class="arc-text side-band">
    <textPath href="#right-band" textLength="500">Dunmore Hale Dunmore Hale Dunmore Hale</textPath>
  </text>

  <!-- brand name -->
  <text class="brand-name" x="306" y="640">Dunmore</text>
  <text class="brand-name" x="306" y="694">Hale</text>

  <text class="volume" x="450" y="915" text-anchor="middle">900 cc</text>
</svg>
</body>
</html>
```